QUICK: Fresh Ideas for New Home Page Design!

Simply improve on our home page design and provide PSD file.

We are Sunward Coverage, a trusted health insurance comparison site to make shopping and enrolling in Carewell easy. We are certified agents for Pacific Shield Exchange, the state's health insurance marketplace (logo attached).

Use flat UI colors.

Looking for a fun design. Reference websites are:
www.plumvista.com
www.hibrindle.com
www.tolmex.com
www.findcanopy.com
www.trymeadowcoverplan.com

Target Market(s)

Individuals ages 18 - 64 shopping for health insurance for themselves and/or their family members. California residents. Don't have health insurance and want it or have it and looking to change.

Industry/Entity Type

Shopping

Font styles to use
Sans Serif

Colors
faed22
33a6d7
33b7a4

Requirements
Must have
• No stock photos. No medical or doctor images or photos. Use images of families. Friendly. Modern fonts and flat UI colors.
Nice to have
• Create a mock-up logo for Sunward Coverage.
Should not have
• No stock looking photos or images

```html
<!DOCTYPE html>
<html lang="en">
<head>
<meta charset="utf-8">
<title>Pacific Shield Exchange – Home</title>
<link href="https://fonts.googleapis.com/css2?family=Open+Sans:wght@300;400;600;700&family=Oswald:wght@300;400&display=swap" rel="stylesheet">
<style>
:root{
  --ink:#4a4850;
  --topbar:#4b4852;
  --yellow:#f7c21b;
  --yellow-dark:#e0a90e;
  --teal:#26b3c6;
  --band:#7ab6e2;
  --text-grey:#8a8a8a;
  --ring-grey:#c9d6d6;
  --white:#ffffff;
}
*{margin:0;padding:0;box-sizing:border-box}
html,body{width:1135px;height:1200px;overflow:hidden;background:var(--white)}
body{position:relative;font-family:"Open Sans",Arial,sans-serif;color:var(--ink)}
.abs{position:absolute}

/* top bar */
.topbar{left:0;top:0;width:1135px;height:33px;background:var(--topbar);color:#fff}
.topbar .parent{left:231px;top:8px;font-size:12.5px;font-weight:300;letter-spacing:.2px}
.topbar .phone{left:616px;top:9px;font-size:11px;display:flex;align-items:center;gap:5px}
.topbar .links{left:739px;top:9px;font-size:10.5px;display:flex;gap:7px}

/* header */
.brand{left:228px;top:56px;display:flex;align-items:center;gap:10px}
.brand .dot{width:44px;height:44px;border-radius:50%;background:var(--teal)}
.brand .name{font-size:17px;font-weight:700;color:var(--ink);letter-spacing:.5px;line-height:1}
.auth{top:48px;height:17px;width:55px;font-size:9px;color:#fff;text-align:center;line-height:17px;border-radius:2px}
.auth.register{left:797px;background:var(--yellow)}
.auth.login{left:857px;background:var(--teal)}
.mainnav{left:514px;top:84px;display:flex;gap:15px;font-size:10px;font-weight:700;color:var(--ink)}
.mainnav .active{position:relative}
.mainnav .active::after{content:"";position:absolute;left:0;right:0;top:17px;height:3px;background:var(--teal)}

/* hero */
.hero{left:0;top:136px;width:1135px;height:342px;background:linear-gradient(180deg,#4f86cf 0%,#9cc3ea 45%,#c9dceb 66%,#7fae3c 80%,#5c8f26 100%)}
.hero-photo{left:560px;top:136px;width:575px;height:342px;background:radial-gradient(ellipse at 60% 60%,rgba(120,150,200,.55),rgba(120,150,200,0) 70%)}
.hero-title{left:231px;top:196px;font-size:22px;font-weight:400;color:#fff;letter-spacing:.3px}
.hero-rule{left:229px;top:232px;width:373px;height:1px;background:rgba(255,255,255,.85)}
.hero-text{left:233px;top:240px;width:360px;font-size:14px;line-height:18px;color:#fff}
.btn{height:33px;background:var(--yellow);color:#fff;font-size:12px;font-weight:600;text-align:center;line-height:33px;border-radius:3px;box-shadow:0 3px 0 var(--yellow-dark)}
.btn.apply{left:237px;top:326px;width:114px}
.btn.find{left:357px;top:326px;width:113px}
.btn.renew{left:476px;top:326px;width:113px}

/* quick links band */
.band{left:0;top:478px;width:1135px;height:53px;background:var(--band)}
.quick{top:488px;display:flex;align-items:center;gap:12px;color:#fff;font-size:14px}

/* stats */
.stat{width:110px;text-align:center;top:574px}
.stat svg{display:block;margin:0 auto}
.stat .num{position:absolute;left:0;right:0;top:24px;font-size:19px;font-weight:300;color:#666}
.stat .label{margin-top:8px;font-size:12px;line-height:14px;color:var(--text-grey)}
.about-title{left:594px;top:543px;font-family:"Oswald",sans-serif;font-weight:300;font-size:20px;color:var(--teal)}
.about-text{left:594px;width:306px;font-size:10.5px;line-height:14.3px;color:var(--text-grey)}

/* help section */
.help{left:0;top:744px;width:1135px;height:456px;background:linear-gradient(90deg,#a48a88 0%,#8c8a6e 35%,#5d6b3c 65%,#4a5a30 100%)}
.help-title{left:0;top:767px;width:1135px;text-align:center;font-size:23px;font-weight:300;color:#fff;letter-spacing:.2px}
.feature{width:170px;text-align:center;color:#fff;font-size:12px;line-height:14px}
.feature svg{display:block;margin:0 auto 8px}
.cta{left:475px;top:1135px;width:173px;height:43px;line-height:43px;font-size:14px}
</style>
</head>
<body>

<header>
  <div class="abs topbar">
    <div class="abs parent">A BRIGHTMERE INSURANCE SERVICES INC. COMPANY</div>
    <div class="abs phone">
      <svg width="11" height="11" viewBox="0 0 11 11"><rect width="11" height="11" rx="2" fill="#f7c21b"/><path d="M3 2.5l1.4 1.4-.8.9a4.5 4.5 0 0 0 2.6 2.6l.9-.8L8.5 8 7.6 9C5 8.8 2.2 6 2 3.4z" fill="#4b4852"/></svg>
      800-555-0142
    </div>
    <nav class="abs links"><span>About Us</span><span>|</span><span>Resources</span><span>|</span><span>Contact Us</span></nav>
  </div>

  <div class="abs brand"><span class="dot"></span><span class="name">PACIFIC SHIELD<br>EXCHANGE</span></div>
  <div class="abs auth register">Register</div>
  <div class="abs auth login">Login</div>
  <nav class="abs mainnav">
    <span class="active">HOME</span><span>HEALTH PLANS</span><span>HEALTH BENEFITS</span><span>AFFORDABLE OPTIONS</span><span>EMPLOYERS</span>
  </nav>
</header>

<section>
  <div class="abs hero" role="img" aria-label="Photo of a father lying on green grass lifting his laughing daughter into a blue sky"></div>
  <div class="abs hero-photo"></div>
  <h1 class="abs hero-title">THIS IS AN EXAMPLE TITLE</h1>
  <div class="abs hero-rule"></div>
  <p class="abs hero-text">Lorem ipsum dolor sit amet, est tedagla copiosae neglegentur intellegebat, ade paulo labores platoriem sit. Te oratioa.</p>
  <div class="abs btn apply">APPLY NOW</div>
  <div class="abs btn find">FIND PLANS</div>
  <div class="abs btn renew">RENEW NOW</div>
</section>

<nav>
  <div class="abs band"></div>
  <div class="abs quick" style="left:245px">
    <svg width="32" height="32" viewBox="0 0 32 32"><circle cx="16" cy="16" r="15" fill="#fff"/><text x="16" y="23" text-anchor="middle" font-family="Open Sans,sans-serif" font-weight="700" font-size="20" fill="#7ab6e2">?</text></svg>
    Do I Qualify?
  </div>
  <div class="abs quick" style="left:414px">
    <svg width="32" height="32" viewBox="0 0 32 32" fill="#fff"><path d="M16 2L2 9v3h28V9z"/><rect x="5" y="13" width="3" height="12"/><rect x="11" y="13" width="3" height="12"/><rect x="18" y="13" width="3" height="12"/><rect x="24" y="13" width="3" height="12"/><rect x="2" y="26" width="28" height="4"/></svg>
    Employers
  </div>
  <div class="abs quick" style="left:588px">
    <svg width="32" height="32" viewBox="0 0 32 32" fill="none" stroke="#fff" stroke-width="4"><path d="M5 22v-6a11 11 0 0 1 22 0v6"/><rect x="3" y="19" width="6" height="9" fill="#fff" stroke="none"/><rect x="23" y="19" width="6" height="9" fill="#fff" stroke="none"/></svg>
    Get Help
  </div>
  <div class="abs quick" style="left:757px">
    <svg width="32" height="32" viewBox="0 0 32 32" fill="#fff"><path d="M1 5h5l4 15h16l4-11H9" fill="none" stroke="#fff" stroke-width="3"/><rect x="9" y="10" width="19" height="8"/><circle cx="12" cy="26" r="3"/><circle cx="24" cy="26" r="3"/></svg>
    Shop + Compare
  </div>
</nav>

<section>
  <div class="abs stat" style="left:226px">
    <svg width="72" height="72" viewBox="0 0 72 72"><circle cx="36" cy="36" r="33" fill="none" stroke="#f7c21b" stroke-width="4"/></svg>
    <div class="num">87%</div>
    <div class="label">of people Qualify for subsides</div>
  </div>
  <div class="abs stat" style="left:343px">
    <svg width="72" height="72" viewBox="0 0 72 72"><circle cx="36" cy="36" r="33" fill="none" stroke="#26b3c6" stroke-width="4"/></svg>
    <div class="num">76%</div>
    <div class="label">Average Discounts After Subsides</div>
  </div>
  <div class="abs stat" style="left:461px">
    <svg width="72" height="72" viewBox="0 0 72 72"><circle cx="36" cy="36" r="33" fill="none" stroke="#c9d6d6" stroke-width="4"/></svg>
    <div class="num">87%</div>
    <div class="label">Average Monthly Premium</div>
  </div>

  <h2 class="abs about-title">THIS IS AN EXAMPLE TITLE</h2>
  <p class="abs about-text" style="top:581px">consequat id duo, cu aeterno indoctum his. Ornatus docendi instructior ex sea. Ei sonet aeterno malorum ius, natum dolorum invenire mea ex, ne eius uscipiantur duo. Pro quando dictas ad. Dolores urbanitas interesset his teele uewan dashen.</p>
  <p class="abs about-text" style="top:656px">Lorem ipsum dolor sit amet, consectetur adipiscing elit. Sed lectus tortor, egestas ut est a, sodales tincidunt risus. Cras ut tortor enim. Morbi ultrices efficitur tortor, ac porttitor est nt erdum sed.</p>
</section>

<section>
  <div class="abs help" role="img" aria-label="Softly tinted photo of a smiling older couple outdoors among green trees"></div>
  <h2 class="abs help-title">HEALTH INSURANCE DOESN’T HAVE TO BE COMPLICATED</h2>

  <div class="abs feature" style="left:270px;top:827px">
    <svg width="74" height="74" viewBox="0 0 74 74"><circle cx="37" cy="37" r="35" fill="none" stroke="#f7c21b" stroke-width="2"/><circle cx="34" cy="34" r="8" fill="none" stroke="#fff" stroke-width="4"/><path d="M40 40l7 7" stroke="#fff" stroke-width="5" stroke-linecap="round"/></svg>
    We help you get<br>financial assistance
  </div>
  <div class="abs feature" style="left:478px;top:827px">
    <svg width="74" height="74" viewBox="0 0 74 74"><circle cx="37" cy="37" r="35" fill="none" stroke="#f7c21b" stroke-width="2"/><rect x="26" y="29" width="19" height="19" rx="3" fill="none" stroke="#fff" stroke-width="2.5"/><path d="M33 41l2-5 11-11 3 3-11 11z" fill="#fff"/></svg>
    We help you choose<br>the right plan
  </div>
  <div class="abs feature" style="left:685px;top:827px">
    <svg width="74" height="74" viewBox="0 0 74 74"><circle cx="37" cy="37" r="35" fill="none" stroke="#f7c21b" stroke-width="2"/><text x="33" y="46" text-anchor="middle" font-family="Open Sans,sans-serif" font-weight="700" font-size="24" fill="#fff">$</text><circle cx="45" cy="43" r="6" fill="#fff"/><path d="M42 42l3 3 3-3" fill="none" stroke="#6b6b50" stroke-width="1.8"/></svg>
    We make sure you get<br>the BEST deal possible
  </div>
  <div class="abs feature" style="left:270px;top:975px">
    <svg width="74" height="74" viewBox="0 0 74 74"><circle cx="37" cy="37" r="35" fill="none" stroke="#f7c21b" stroke-width="2"/><ellipse cx="34" cy="35" rx="12" ry="8" fill="#fff"/><path d="M28 41l-4 6 8-4z" fill="#fff"/><ellipse cx="41" cy="40" rx="9" ry="6" fill="#fff" stroke="#8a7f68" stroke-width="1.5"/></svg>
    We help you<br>enroll
  </div>
  <div class="abs feature" style="left:478px;top:975px">
    <svg width="74" height="74" viewBox="0 0 74 74"><circle cx="37" cy="37" r="35" fill="none" stroke="#f7c21b" stroke-width="2"/><circle cx="37" cy="37" r="12" fill="#fff"/><path d="M42 31l-3 8-7 4 3-8z" fill="#7a7660"/></svg>
    We navigate you<br>through health reform
  </div>
  <div class="abs feature" style="left:685px;top:975px">
    <svg width="74" height="74" viewBox="0 0 74 74"><circle cx="37" cy="37" r="35" fill="none" stroke="#f7c21b" stroke-width="2"/><path d="M24 37a13 13 0 0 1 26 0z" fill="#fff"/><path d="M37 37v10a3 3 0 0 1-6 0" fill="none" stroke="#fff" stroke-width="2.5"/><path d="M37 22v3" stroke="#fff" stroke-width="2"/></svg>
    We help you get<br>financial assistance
  </div>

  <div class="abs btn cta">LET US HELP YOU</div>
</section>

</body>
</html>
```